Tranquil Pathway Business Card

Logo attached. (will be printing onto thick white/off white textured card)

Double sided business card for two Therapists working at Tranquil Pathway.

Require one design, but with different name and mobile numbers on each card.

Target Market(s)

Medical, Health

Industry/Entity Type

Business

Contact Information for Business Card

Need one business card design, but a separate card for each person - Colin Marchetti and Marieke de Boeckx.

FRONT OF CARD

Logo

Name (Colin Marchetti on one card, Marieke de Boeckx on the other)
Professional Clinical Hypnotherapist

Consulting Rooms (Near Lindqvist Hospital)
482 Brackenfield Road
Dunmore VIC 3987

Colin@TranquilPathway.example.au OR Marieke@TranquilPathway.example.au

Mobile: 0455 872 604 (for Colin) OR
Mobile: 0467 290 518 (for Marieke)

BACK OF CARD

Logo

Website: www.TranquilPathway.example.au

Phone: 1300 958 471

Requirements
Must have
• Text and logo only. No additiional graphics.

```html
<!DOCTYPE html>
<html lang="en">
<head>
<meta charset="utf-8">
<title>Tranquil Pathway Business Card</title>
<link rel="stylesheet" href="https://fonts.googleapis.com/css2?family=Open+Sans:wght@400;700&family=Arimo:wght@400&display=swap">
<style>
  :root {
    --navy: #212a5c;
    --grey: #707070;
    --ink: #111111;
    --rule: #555555;
    --paper: #ffffff;
  }
  * { margin: 0; padding: 0; box-sizing: border-box; }
  html, body { width: 1200px; height: 1200px; overflow: hidden; background: var(--paper); }
  .sheet {
    position: relative; width: 1200px; height: 1200px;
    border: 2px solid #222; background: var(--paper);
    font-family: "Open Sans", Arial, sans-serif;
  }
  .card {
    position: absolute; left: 264px; width: 693px;
    border: 1px solid var(--rule); background: var(--paper); overflow: hidden;
  }
  .card--front { top: 145px; height: 419px; }
  .card--back { top: 650px; height: 418px; }

  .brand { position: absolute; display: flex; align-items: center; color: var(--navy); font-weight: 700; }
  .brand__dot { border-radius: 50%; background: var(--navy); flex: none; }
  .brand--small { left: 39px; top: 31px; gap: 14px; font-size: 18px; letter-spacing: 0.5px; }
  .brand--small .brand__dot { width: 62px; height: 62px; }
  .brand--large { left: 116px; top: 106px; gap: 28px; font-size: 40px; line-height: 1.05; letter-spacing: 1px; }
  .brand--large .brand__dot { width: 148px; height: 148px; }

  .holder { position: absolute; left: 0; right: 0; top: 174px; text-align: center; color: var(--ink); }
  .holder__name { font-size: 43px; font-weight: 400; line-height: 1; }
  .holder__role { font-size: 16.5px; line-height: 1.2; margin-top: 2px; padding-left: 6px; }

  .contact-band {
    position: absolute; left: 0; right: 0; bottom: 0; height: 79px;
    background: var(--navy); color: #fff; font-size: 14.5px; line-height: 19px;
  }
  .contact-band__address { position: absolute; left: 32px; top: 10px; }
  .contact-band__direct { position: absolute; left: 343px; top: 23px; }
  .contact-band__label { display: inline-block; width: 52px; }

  .web-details {
    position: absolute; left: 0; right: 0; top: 325px; text-align: center;
    font-family: "Arimo", Arial, sans-serif; font-size: 14px; line-height: 24px; color: var(--grey);
  }
</style>
</head>
<body>
<div class="sheet">
  <section class="card card--front">
    <div class="brand brand--small"><span class="brand__dot"></span><span class="brand__name">TRANQUIL PATHWAY</span></div>
    <div class="holder">
      <h1 class="holder__name">Colin Marchetti</h1>
      <p class="holder__role">Professional Clinical Hypnotherapist</p>
    </div>
    <div class="contact-band">
      <p class="contact-band__address">Consulting Rooms (Near Lindqvist Hospital)<br>482 Brackenfield Road<br>Dunmore VIC 3987</p>
      <p class="contact-band__direct"><span class="contact-band__label">Mobile</span>: 0455 872 604<br><span class="contact-band__label">E-Mail</span>: Colin@TranquilPathway.example.au</p>
    </div>
  </section>

  <section class="card card--back">
    <div class="brand brand--large"><span class="brand__dot"></span><span class="brand__name">TRANQUIL<br>PATHWAY</span></div>
    <p class="web-details">www.TranquilPathway.example.au<br>Phone: 1300 958 471</p>
  </section>
</div>
</body>
</html>
```